Forest Consultant/Timber Buyer needs a clean business card

We are a forestry consulting and timber buying company. We meet with private landowners and assist them with timber management and timber harvesting. We would like a professional business card, please no clip art. logo is blue and white but would like to see a gray,silver, or some other color incorporated. Would like basic contact info. Would like to the layout to be creative and sleek but masculine.

Target Market(s)

private landowners

Industry/Entity Type

Business

Contact Information for Business Card

name,position, cell number, office number, email, website. This might be to cluttered. Basic contact info is what we are looking for.

Contact info can all be on one side with logo on the other.

Font styles to use
Serif
Sans Serif

Colors
0255a3
ffffff
aaaaaa

Requirements
Must have
• We just want it professional.
Nice to have
• Creative layout.
Should not have
• please no clip art of log trucks etc.

```html
<!DOCTYPE html>
<html lang="en">
<head>
<meta charset="utf-8">
<title>Ridgeline Forestry — Business Card</title>
<link href="https://fonts.googleapis.com/css2?family=Roboto:wght@400;700&display=swap" rel="stylesheet">
<style>
  :root {
    --brand-blue: #0255a3;
    --silver: #aaaaaa;
    --white: #ffffff;
  }
  html, body {
    margin: 0;
    padding: 0;
    width: 1200px;
    height: 706px;
    overflow: hidden;
    background: var(--white);
  }
  .card {
    position: relative;
    width: 1200px;
    height: 706px;
    overflow: hidden;
    background: var(--white);
    font-family: "Roboto", Arial, sans-serif;
    color: var(--white);
  }
  .card__shapes {
    position: absolute;
    inset: 0;
    width: 1200px;
    height: 706px;
  }
  .brand {
    position: absolute;
    left: 30px;
    top: 268px;
    width: 500px;
    display: flex;
    align-items: center;
    justify-content: center;
    gap: 16px;
    color: var(--brand-blue);
  }
  .brand__dot {
    width: 26px;
    height: 26px;
    border-radius: 50%;
    background: var(--brand-blue);
    flex: none;
  }
  .brand__name {
    font-size: 46px;
    font-weight: 700;
    line-height: 1;
    white-space: nowrap;
  }
  .person {
    position: absolute;
    right: 41px;
    top: 156px;
    text-align: right;
    line-height: 1;
  }
  .person__name {
    font-size: 43px;
    font-weight: 400;
    letter-spacing: 0.5px;
  }
  .person__name strong { font-weight: 700; }
  .person__title {
    margin-top: 6px;
    font-size: 38px;
    font-weight: 400;
    letter-spacing: 0.5px;
  }
  .contact {
    position: absolute;
    text-align: right;
    line-height: 1;
    white-space: nowrap;
  }
  .contact--phone {
    right: 146px;
    top: 496px;
    font-size: 31px;
  }
  .contact--phone .contact__line + .contact__line { margin-top: 14px; }
  .contact--web {
    right: 139px;
    top: 610px;
    font-size: 22px;
  }
  .contact--web .contact__line + .contact__line { margin-top: 17px; }
</style>
</head>
<body>
<div class="card">
  <svg class="card__shapes" viewBox="0 0 1004 591" preserveAspectRatio="none" aria-hidden="true">
    <polygon class="shape-top-band" points="318,0 1004,0 1004,241 470,241" fill="var(--silver)"/>
    <polygon class="shape-accent-stripe" points="290,0 305,0 462,246 449,246" fill="var(--brand-blue)"/>
    <polygon class="shape-bottom-panel" points="467,254 1004,254 1004,591 275,591" fill="var(--brand-blue)"/>
    <polygon class="shape-corner-wedge" points="0,591 0,565 454,250 262,591" fill="var(--silver)"/>

    <polygon class="phone-rule" points="568,445 892,441 912,446 900,462 890,448 568,447" fill="var(--white)"/>
    <g class="icon-phone" fill="var(--white)">
      <path d="M912,433 q0,-12 29,-12 q29,0 29,12 l0,6 l-12,0 l0,-6 l-34,0 l0,6 l-12,0 z"/>
      <path d="M922,441 l38,0 l8,22 l-54,0 z"/>
      <circle cx="941" cy="451" r="7" fill="var(--brand-blue)"/>
    </g>

    <polygon class="email-rule" points="565,536 892,532 912,537 900,553 890,539 565,538" fill="var(--white)"/>
    <g class="icon-mail">
      <rect x="913" y="517" width="57" height="38" fill="var(--white)"/>
      <polyline points="913,517 941,540 970,517" fill="none" stroke="var(--brand-blue)" stroke-width="3"/>
      <line x1="913" y1="555" x2="933" y2="534" stroke="var(--brand-blue)" stroke-width="2"/>
      <line x1="970" y1="555" x2="950" y2="534" stroke="var(--brand-blue)" stroke-width="2"/>
    </g>
  </svg>

  <div class="brand">
    <span class="brand__dot"></span>
    <span class="brand__name">Ridgeline Forestry</span>
  </div>

  <div class="person">
    <div class="person__name"><strong>DAN</strong>HOLLIS</div>
    <div class="person__title">DIRECTOR</div>
  </div>

  <div class="contact contact--phone">
    <div class="contact__line">+ 000 - 0000 - 0000</div>
    <div class="contact__line">+ 000 - 0000 - 0000</div>
  </div>

  <div class="contact contact--web">
    <div class="contact__line">office@ridgelineforestry.com</div>
    <div class="contact__line">ridgelineforestry.com</div>
  </div>
</div>
</body>
</html>
```